Crime/mystery/thriller novel cover design

I am looking to get a cover designed for a novel. It is a crime/mystery/thriller set in Liverpool, England, between the 1970s and current day. I have permission to use some paintings by an artist for the cover, so it just needs put together and jazzed up. I am looking for something which has a fairly classic feel (so not just pulp airport thriller trash) but with some flair nonetheless.
The novel will be paperback, 127mm x 203mm with approx 18mm spine width. Can be gloss or matt cover, would be interesting to discuss.
The title is:
THE HARBOUR LANTERN
Author name:
GORDON T. VESELKA
Publisher:
BRIVOLTA PUBLISHING LTD (or simply BRIVOLTA)

I am still working on the back cover blurb but I will upload this when finished.
There are 4 images I could use for the cover though my favourite is the one called Dusk, Quayside Terraces.

```html
<!DOCTYPE html>
<html lang="en">
<head>
<meta charset="utf-8">
<title>The Harbour Lantern — Front Cover</title>
<link href="https://fonts.googleapis.com/css2?family=Oswald:wght@500;600;700&display=swap" rel="stylesheet">
<style>
  :root {
    --page: #ffffff;
    --ink-light: #f4f4f2;
    --sky-deep: #1f2d2e;
    --sky-teal: #3f7a78;
    --sky-green: #6f8a4f;
    --sunset-gold: #c98a3e;
    --sunset-orange: #b5602c;
    --skyline-dark: #3a2620;
    --water-navy: #15203a;
    --water-rust: #9a5328;
    --water-blue: #1f2c5e;
  }
  html, body {
    margin: 0;
    padding: 0;
    width: 1200px;
    height: 1200px;
    overflow: hidden;
    background: var(--page);
  }
  .canvas {
    position: relative;
    width: 1200px;
    height: 1200px;
  }
  .front-cover {
    position: absolute;
    left: 256px;
    top: 50px;
    width: 688px;
    height: 1100px;
    overflow: hidden;
    background: var(--water-navy);
    box-shadow: 0 6px 24px rgba(0,0,0,0.18);
  }
  .cover-painting {
    position: absolute;
    inset: 0;
    background:
      radial-gradient(ellipse 60% 18% at 45% 22%, rgba(111,138,79,0.75), transparent 70%),
      radial-gradient(ellipse 35% 12% at 20% 20%, rgba(63,122,120,0.8), transparent 70%),
      radial-gradient(ellipse 70% 14% at 50% 45%, rgba(201,138,62,0.8), transparent 75%),
      radial-gradient(ellipse 70% 12% at 50% 78%, rgba(154,83,40,0.85), transparent 75%),
      linear-gradient(180deg,
        var(--sky-deep) 0%,
        #2c4541 12%,
        var(--sky-green) 24%,
        var(--sunset-gold) 36%,
        var(--sunset-orange) 44%,
        var(--skyline-dark) 52%,
        #2a2220 57%,
        var(--water-navy) 63%,
        #24263a 70%,
        var(--water-rust) 78%,
        #3a2e3e 86%,
        var(--water-blue) 94%,
        #182250 100%);
  }
  .cover-text {
    position: absolute;
    inset: 0;
    font-family: 'Oswald', 'Arial Narrow', sans-serif;
    color: var(--ink-light);
    text-transform: uppercase;
  }
  .author-name {
    position: absolute;
    top: 48px;
    left: 0;
    right: 0;
    text-align: center;
    font-weight: 600;
    font-size: 26px;
    letter-spacing: 0.72em;
    padding-left: 0.72em;
    margin: 0;
  }
  .book-title {
    position: absolute;
    top: 500px;
    left: 0;
    right: 0;
    margin: 0;
    text-align: center;
    font-weight: 700;
    line-height: 1;
  }
  .title-article {
    display: block;
    font-size: 34px;
    font-weight: 600;
    letter-spacing: 0.6em;
    padding-left: 0.6em;
  }
  .title-main {
    display: block;
    font-size: 150px;
    letter-spacing: 0.01em;
    margin-top: 4px;
    line-height: 0.95;
  }
  .title-sub {
    display: block;
    font-size: 58px;
    font-weight: 600;
    letter-spacing: 0.62em;
    padding-left: 0.62em;
    margin-top: 8px;
  }
  .publisher-name {
    position: absolute;
    right: 44px;
    bottom: 38px;
    margin: 0;
    font-size: 15px;
    font-weight: 600;
    letter-spacing: 0.28em;
  }
</style>
</head>
<body>
  <main class="canvas">
    <section class="front-cover">
      <div class="cover-painting" role="img" aria-label="Painting: Dusk, Quayside Terraces — waterfront skyline under a swirling green and orange sky, reflected in the dark river"></div>
      <div class="cover-text">
        <p class="author-name">Gordon T. Veselka</p>
        <h1 class="book-title">
          <span class="title-article">The</span>
          <span class="title-main">Harbour</span>
          <span class="title-sub">Lantern</span>
        </h1>
        <p class="publisher-name">Brivolta Publishing Ltd</p>
      </div>
    </section>
  </main>
</body>
</html>
```